Professional / Luxury Rack Card Design Needed (Do not use AI)

We are a private, boutique style optometry practice in College Station, Texas. We want the new design to communicate a premium, modern, luxury eye care experience while remaining professional and approachable.
When someone picks up this rack card, we want them to think:
"This practice looks modern, advanced, trustworthy, and premium. I would expect exceptional care and a high-end eyewear experience."

Target Market(s)

Families, professionals, adults seeking comprehensive medical eye care and vision correction. Patients seeking premium eyewear, advanced technology, and personalize care. Individuals and families seeking long term relationships with a trusted eye care provider. Patients who value exceptional service, expertise, and convenience.

Industry/Entity Type

Medical & Optometry-luxury optical

Font styles to use
Serif
Other font styles liked:
• Avenir if available. If not, Montserrat for headlines and Open Sans for Body text. For the slogan, use larger bold Montserrat.

Requirements
Must have
• Non-edited photo of doctors (merged together) with names. "Your Vision. Our Focus." Phone, website, Text/Call to Schedule appointment (Call to action to schedule). Accepting new patients. Eye Care center logo prominently displayed. Real photo of Eye Care Center building. Contact information (see attachement with all info)
Nice to have
• For frame brands, use the branded names. (see attachment)
Should not have
• Shouild not be busy/cluttered. Do not use scripted font from my website. Do NOT use AI generated images. Do not edit doctor faces other than merging them together. DO NOT use AI to edit faces....only to merge them side by side.

```html
<!DOCTYPE html>
<html lang="en">
<head>
<meta charset="utf-8">
<title>Clearview Eye Studio – Rack Card</title>
<link rel="stylesheet" href="https://fonts.googleapis.com/css2?family=Jost:wght@400;500;600&family=Open+Sans:wght@400;600;700&display=swap">
<style>
  :root{
    --backdrop:#a8dce8;
    --paper:#ffffff;
    --ink-grey:#6d6e71;
    --ink-dark:#231f20;
    --accent-blue:#a3dbe8;
    --accent-gold:#e0b22c;
    --footer:#231f20;
  }
  *{box-sizing:border-box;margin:0;padding:0}
  html,body{width:1200px;height:1000px;overflow:hidden}
  body{background:var(--backdrop);position:relative;font-family:"Open Sans",Arial,sans-serif}
  .card{position:absolute;top:176px;width:288px;height:648px;background:var(--paper);overflow:hidden}
  .card--front{left:298px}
  .card--back{left:613px}
  .card__art{position:absolute;inset:0}

  .brand{position:absolute;top:26px;left:0;width:100%;text-align:center}
  .brand__name{display:inline-flex;align-items:center;gap:8px;font-family:"Jost",sans-serif;font-weight:400;font-size:23px;color:var(--ink-grey);letter-spacing:.2px}
  .brand__dot{width:22px;height:22px;border-radius:50%;background:var(--accent-blue)}
  .brand__member{margin-top:2px;font-size:7px;letter-spacing:1px;text-transform:uppercase;color:var(--ink-grey);padding-left:40px}

  .headline{position:absolute;top:276px;width:100%;text-align:center;font-family:"Jost",sans-serif;font-weight:600;font-size:28px;line-height:30px;color:var(--ink-grey)}
  .cta{position:absolute;top:344px;left:23px;width:242px;height:38px;border-radius:19px;background:var(--accent-blue);display:flex;align-items:center;justify-content:center;font-weight:700;font-size:12px;color:var(--ink-dark)}
  .note{position:absolute;top:391px;width:100%;text-align:center;font-size:12px;color:var(--ink-grey)}
  .web{position:absolute;top:612px;height:36px;width:100%;display:flex;align-items:center;justify-content:center;font-size:12px;font-weight:600;color:var(--accent-gold)}

  .services{position:absolute;top:314px;left:50px}
  .services__title{font-family:"Jost",sans-serif;font-weight:600;font-size:23px;color:var(--ink-grey);margin-bottom:3px}
  .services__list{list-style:none}
  .services__list li{font-size:12.5px;line-height:18px;color:var(--ink-grey);padding-left:10px;position:relative}
  .services__list li::before{content:"";position:absolute;left:0;top:7px;width:3px;height:3px;border-radius:50%;background:var(--accent-gold)}

  .contact{position:absolute;top:518px;left:0;width:100%;height:130px;background:var(--footer);color:#fff}
  .contact__row{position:absolute;display:flex;align-items:center;gap:8px}
  .contact__row--address{top:26px;left:50px}
  .contact__row--phone{top:78px;left:56px;gap:10px}
  .contact__address{font-size:9px;font-weight:700;line-height:13px}
  .contact__address small{display:block;font-size:7px;font-weight:600}
  .contact__phone{font-family:"Jost",sans-serif;font-weight:600;font-size:23px}
</style>
</head>
<body>

<section class="card card--front">
  <svg class="card__art" width="288" height="648" viewBox="0 0 288 648">
    <defs>
      <linearGradient id="interiorTone" x1="0" y1="0" x2="1" y2="1">
        <stop offset="0" stop-color="#8a7560"/>
        <stop offset=".5" stop-color="#3d342d"/>
        <stop offset="1" stop-color="#6c7f86"/>
      </linearGradient>
      <linearGradient id="buildingTone" x1="0" y1="0" x2="0" y2="1">
        <stop offset="0" stop-color="#c9d3dc"/>
        <stop offset=".45" stop-color="#d9c6a4"/>
        <stop offset="1" stop-color="#8d6e4e"/>
      </linearGradient>
    </defs>
    <path role="img" aria-label="Photo of the practice interior with stone wall, reception desk and eyewear displays" d="M0 83H288V222C236 250 160 238 100 258C60 270 26 278 0 285Z" fill="url(#interiorTone)"/>
    <path role="img" aria-label="Photo of the practice building exterior with signage" d="M0 438C80 412 200 420 288 392V612H0Z" fill="url(#buildingTone)"/>
    <rect x="0" y="612" width="288" height="36" fill="var(--footer)"/>
  </svg>

  <div class="brand">
    <div class="brand__name"><span class="brand__dot"></span>clearview eye studio</div>
    <div class="brand__member">A member of Optic Alliance</div>
  </div>

  <h1 class="headline">Your Vision.<br>Our Focus.</h1>
  <div class="cta">Schedule your appointment today</div>
  <p class="note">Accepting new patients.</p>
  <p class="web">www.clearvieweyestudio.com</p>
</section>

<section class="card card--back">
  <svg class="card__art" width="288" height="648" viewBox="0 0 288 648">
    <defs>
      <linearGradient id="stoneTone" x1="0" y1="0" x2="1" y2="1">
        <stop offset="0" stop-color="#c4ab8a"/>
        <stop offset="1" stop-color="#9c8062"/>
      </linearGradient>
      <linearGradient id="teamTone" x1="0" y1="0" x2="0" y2="1">
        <stop offset="0" stop-color="#f2f0ed"/>
        <stop offset=".6" stop-color="#e3e0dc"/>
        <stop offset=".8" stop-color="#8a817b"/>
        <stop offset="1" stop-color="#3b3433"/>
      </linearGradient>
    </defs>
    <path role="img" aria-label="Stone wall backdrop" d="M0 0H288V45C240 140 130 150 70 175C40 188 15 195 0 200Z" fill="url(#stoneTone)"/>
    <path role="img" aria-label="Photo of the four doctors standing together in white coats" d="M52 96C52 66 74 44 104 42H196C224 44 244 66 244 96V262C244 274 236 282 224 282H72C60 282 52 274 52 262Z" fill="url(#teamTone)"/>
  </svg>

  <div class="services">
    <h2 class="services__title">Services</h2>
    <ul class="services__list">
      <li>Comprehensive Eye Exams</li>
      <li>Contact Lens Specialists</li>
      <li>Pediatric Exams</li>
      <li>LASIK Co-Management</li>
      <li>Cataracts &amp; Glaucoma Treatment</li>
      <li>Dry Eye &amp; Allergy Treatments</li>
      <li>Eye Injuries &amp; Infections</li>
      <li>Ocular Disease Management</li>
    </ul>
  </div>

  <div class="contact">
    <div class="contact__row contact__row--address">
      <svg width="28" height="36" viewBox="0 0 28 36" aria-hidden="true">
        <path d="M14 2C7.4 2 2.5 7 2.5 13.3 2.5 22 14 34 14 34S25.5 22 25.5 13.3C25.5 7 20.6 2 14 2Z" fill="none" stroke="var(--accent-blue)" stroke-width="2.6"/>
        <circle cx="14" cy="13.5" r="4" fill="none" stroke="var(--accent-blue)" stroke-width="2.6"/>
      </svg>
      <p class="contact__address">418 Meadow Ridge Pkwy<br>Brazos Falls, TX 77850<small>Conveniently located in Oakline Plaza</small></p>
    </div>
    <div class="contact__row contact__row--phone">
      <svg width="18" height="24" viewBox="0 0 20 26" aria-hidden="true">
        <path d="M7 2C4 3 2 6 2.5 11 3.5 18 8 23 13 24.5 15 25 17 23.5 18 21.5L14.5 17.5 11.5 19C9 16.5 8 13 8 10L11 8.5 9.5 2.5Z" fill="var(--accent-blue)"/>
      </svg>
      <span class="contact__phone">555-014-2290</span>
    </div>
  </div>
</section>

</body>
</html>
```